Heavy Duty Repairs Poster

Good afternoon - I'm looking for a poster , design to set up around different areas. The Poster must consist of the following
- Heavy duty repairs
- Pictures of Semi trucks , heavy construction equipment , trailers
- Agriculture
- All north American equipment ( see attached pictures)
- Brief Descriptions in bullet point forms
CVIPS
WELDING
AIR CONDITIONING
ENGINE REBUILDS
DIAGONSTICS
FLEET MANAGMENT
TIRE REPAIR AND SALES
ELECTRICAL , HYDRALIC , POWER TRAIN SERVICE AND REPAIRS
PART SALES
FLEET MAINTINACE
DELTEING AND TUNING
AFTER MARKET INSTALLS OUTFITTING
ONSITE & OFFSITE REPAIRS
FULL RECERTIFACTION OVERHAULING
Warranty Approved

Target Market(s)

Heavy Duty Truck , Equipment , Agriculture Owners

Industry/Entity Type

Heavy Duty Repairs

Colors
EB3D1F
EC4F4E
F09395
F8D3D4
FCEDEE

Requirements
Must have
• Pictures of : Semi trucks and trailer , Construction heavy equipment , agriculture equipment
Nice to have
• Flashy and stands out

```html
<!DOCTYPE html>
<html lang="en">
<head>
<meta charset="utf-8">
<title>Heavy Duty Repair</title>
<link href="https://fonts.googleapis.com/css2?family=Bebas+Neue&family=Rajdhani:wght@500;600&family=Montserrat:wght@600;700&family=Tinos:wght@400;700&display=swap" rel="stylesheet">
<style>
  :root {
    --sky-top: #1550d6;
    --sky-mid: #3b74c4;
    --ground: #1b1d20;
    --ink-dark: #0b0b0c;
    --accent: #e6a033;
    --white: #ffffff;
    --phone-red: #e0403a;
    --machine-yellow: #d9a92c;
  }
  * { margin: 0; padding: 0; box-sizing: border-box; }
  html, body { width: 926px; height: 1200px; overflow: hidden; }
  body { background: var(--ground); }
  .poster {
    position: relative;
    width: 926px;
    height: 1200px;
    overflow: hidden;
    background: linear-gradient(180deg, var(--sky-top) 0%, var(--sky-mid) 28%, #4a6f96 44%, #2a3440 60%, var(--ground) 78%, #141517 100%);
    font-family: "Rajdhani", sans-serif;
    color: var(--white);
  }
  .accent-block {
    position: absolute; left: 0; top: 105px; width: 121px; height: 291px;
    background: var(--accent);
  }
  .headline {
    position: absolute; left: 145px; top: 96px;
    font-family: "Bebas Neue", sans-serif;
    font-size: 134px; line-height: 104px;
    letter-spacing: -2px;
    text-shadow: 4px 5px 8px rgba(0,0,0,0.35);
  }
  .brand-box {
    position: absolute; left: 599px; top: 0; width: 222px; height: 136px;
    background: var(--ink-dark);
    border-radius: 0 0 10px 10px;
    text-align: center;
    font-family: "Tinos", serif;
  }
  .brand-phone {
    margin-top: 34px;
    font-family: "Montserrat", sans-serif;
    font-weight: 700; font-size: 19px; color: var(--phone-red);
  }
  .brand-name { margin-top: 20px; font-size: 14px; font-weight: 400; }
  .brand-place { font-size: 11px; margin-top: 2px; }
  .machinery {
    position: absolute; left: 120px; top: 370px; width: 660px; height: 294px;
    background: radial-gradient(ellipse at 60% 60%, var(--machine-yellow) 0%, #a9801f 45%, rgba(40,40,40,0) 75%);
  }
  .offer-panel {
    position: absolute; left: 136px; top: 653px; width: 644px; height: 432px;
    background: linear-gradient(180deg, rgba(11,11,12,0.2) 0%, rgba(11,11,12,0.9) 18%, var(--ink-dark) 40%);
  }
  .offer-title {
    position: absolute; left: 173px; top: 712px;
    font-family: "Montserrat", sans-serif; font-weight: 600; font-size: 31px;
    padding-bottom: 2px; border-bottom: 2px solid var(--white);
  }
  .service-list {
    position: absolute; top: 784px; list-style: none;
    font-size: 19px; font-weight: 500; letter-spacing: 0.6px; line-height: 23px;
  }
  .service-list li { position: relative; padding-left: 27px; margin-bottom: 10px; }
  .service-list li::before {
    content: ""; position: absolute; left: 0; top: 8px; width: 8px; height: 8px;
    background: var(--white);
  }
  .col-left { left: 173px; width: 250px; }
  .col-right { left: 439px; width: 330px; }
  .accent-rule {
    position: absolute; left: 136px; top: 1088px; width: 644px; height: 7px;
    background: var(--accent);
  }
  .footer-phone {
    position: absolute; left: 0; top: 1120px; width: 926px; text-align: center;
    font-family: "Montserrat", sans-serif; font-weight: 700; font-size: 34px;
    letter-spacing: 8px;
  }
</style>
</head>
<body>
<main class="poster">
  <div class="accent-block"></div>
  <h1 class="headline">HEAVY<br>DUTY<br>REPAIR</h1>

  <div class="brand-box">
    <div class="brand-phone">555-214-0837</div>
    <div class="brand-name">Ironridge Mechanical Services</div>
    <div class="brand-place">Cedar Flats, Alberta</div>
  </div>

  <div class="machinery" role="img" aria-label="Row of yellow heavy equipment: farm tractor, semi truck, mining dump truck and tracked excavator"></div>

  <div class="offer-panel"></div>
  <h2 class="offer-title">We are Offering</h2>

  <ul class="service-list col-left">
    <li>CVIPS</li>
    <li>Welding</li>
    <li>Air Conditioning</li>
    <li>Engine Rebuilds</li>
    <li>Diagonstics</li>
    <li>Fleet Managment</li>
    <li>Electrical, Hydralic,<br>Power Train Service<br>and Repairs</li>
  </ul>
  <ul class="service-list col-right">
    <li>Part Sales</li>
    <li>Fleet Maintinace</li>
    <li>Delteing And Tuning</li>
    <li>After Market Installs Outfitting</li>
    <li>Onsite &amp; Offsite Repairs</li>
    <li>Tire Repair And Sales</li>
    <li>Full Recertifaction Overhauling</li>
  </ul>

  <div class="accent-rule"></div>
  <div class="footer-phone">555-214-0837</div>
</main>
</body>
</html>
```